Hello - our company Dravenmoor Health develops novel dietary supplements. We're looking for a label design for a new product. The product is a premium MALE ENHANCEMENT supplement. Below is a link to other competitive products on Vantiro. We’re looking for a powerful, dynamic design. The bottle will be a white 150cc supplement bottle.

The product name is Zentaric

https://www.vantiro-example.com/s?k=male+enhancement&crid=QTRWPZ4MX81N&sprefix=male+enhancement%2Caps%2C52&ref=nb_sb_noss_2

Label size in inches - Rectangle 5.5"w x 2.5"h

```html
<!DOCTYPE html>
<html lang="en">
<head>
<meta charset="utf-8">
<title>Zentaric Label</title>
<link rel="stylesheet" href="https://fonts.googleapis.com/css2?family=Arimo:wght@400;700&family=Saira:ital,wght@1,700;1,800;1,900&display=swap">
<style>
  :root{
    --ink:#1c1c1e;
    --panel:#1f1f21;
    --blue:#1f5cc4;
    --white:#ffffff;
    --page:#f3f3f3;
    --text:#1a1a1a;
  }
  *{margin:0;padding:0;box-sizing:border-box}
  html,body{width:1200px;height:675px;overflow:hidden;background:var(--page)}
  .label{
    position:absolute;left:20px;top:74px;width:1456px;height:662px;
    background:var(--white);transform:scale(0.7967);transform-origin:0 0;
    font-family:Arimo,Arial,sans-serif;color:var(--text);
    box-shadow:0 4px 18px rgba(0,0,0,.12);
  }
  .label-shape{position:absolute;inset:0}
  .info{position:absolute;left:71px;top:49px;width:412px;font-size:16.5px;line-height:20.5px}
  .info p{margin-bottom:21px}
  .info .desc{margin-bottom:28px}
  .info .storage{margin-top:24px}
  .disclaimer{
    position:absolute;left:70px;top:343px;width:414px;height:81px;border:3px solid var(--text);
    font-size:15px;line-height:19px;text-align:center;padding:7px 4px;letter-spacing:-0.15px;
    display:flex;align-items:center;justify-content:center;
  }
  .barcode-box{
    position:absolute;left:68px;top:448px;width:209px;height:94px;border:3px solid var(--text);
    display:flex;align-items:center;justify-content:center;font-size:19px;
  }
  .maker{position:absolute;left:286px;top:447px;font-size:15.5px;line-height:18.5px;font-weight:700;white-space:nowrap}
  .vertical{
    position:absolute;writing-mode:vertical-rl;transform:rotate(180deg);
    font-family:Saira,Arial,sans-serif;font-style:italic;text-transform:uppercase;
    display:flex;align-items:center;justify-content:center;white-space:nowrap;
  }
  .extra-strength{left:584px;top:97px;width:30px;height:275px;background:var(--ink);color:var(--white);font-weight:800;font-size:21px;letter-spacing:2px}
  .product-name{left:632px;top:96px;width:66px;height:462px;color:var(--blue);font-weight:900;font-size:76px;letter-spacing:1px;line-height:1}
  .category{left:724px;top:100px;width:50px;height:372px;color:var(--white);font-weight:800;font-size:22px;line-height:25px;letter-spacing:2.5px;text-align:right;align-items:flex-start}
  .dose{left:815px;top:110px;width:44px;height:268px;background:var(--blue);color:var(--white);font-weight:900;font-size:40px;letter-spacing:1px;clip-path:polygon(0 0,100% 6%,100% 100%,0 100%)}
  .benefits{position:absolute;left:752px;top:458px;width:122px;list-style:none}
  .benefits li{
    font-family:Saira,Arial,sans-serif;font-style:italic;font-weight:900;font-size:19px;color:var(--white);
    text-align:right;letter-spacing:1px;height:41px;padding-top:6px;border-bottom:3px solid var(--blue);
  }
  .footer{position:absolute;left:0;right:0;top:612px;height:50px;display:flex;align-items:center}
  .footer span{font-family:Saira,Arial,sans-serif;font-style:italic;font-weight:900;font-size:19px;color:var(--white);letter-spacing:2.5px}
  .footer .count{position:absolute;left:505px}
  .footer .divider{position:absolute;left:692px;top:9px;width:3px;height:32px;background:var(--white)}
  .footer .kind{position:absolute;left:720px}
  .facts{
    position:absolute;left:1032px;top:47px;width:370px;height:452px;border:3px solid var(--blue);
    border-radius:20px;overflow:hidden;color:var(--white);background:var(--panel);font-size:14px;
  }
  .facts h2{background:var(--blue);height:42px;font-family:Arimo,Arial,sans-serif;font-weight:700;font-size:31px;text-align:center;line-height:44px;letter-spacing:.5px}
  .serving{display:flex;justify-content:space-between;padding:0 10px 0 12px;height:36px;align-items:center;font-size:14px;border-bottom:5px solid var(--blue)}
  .amount-head{display:flex;justify-content:flex-end;gap:12px;padding-right:14px;font-weight:700;font-size:12.5px;height:30px;align-items:center;border-bottom:2px solid var(--blue)}
  .row{position:relative;padding:4px 0 0 12px;border-bottom:2px solid var(--blue);line-height:15px}
  .row small{display:block;font-size:11px;line-height:13px;padding-left:16px}
  .row .amt{position:absolute;right:56px;top:4px}
  .row .dv{position:absolute;right:28px;top:4px}
  .facts .note{border-top:6px solid var(--blue);padding:8px 12px;font-size:14px}
  .other{position:absolute;left:1044px;top:508px;width:370px;font-size:17px;line-height:21px;color:var(--white)}
  .badges{position:absolute;left:1074px;top:566px;display:flex;gap:10px}
  .badges span{width:62px;height:62px;border-radius:50%;background:var(--white);border:4px solid #8a8a8a}
</style>
</head>
<body>
<div class="label">
  <svg class="label-shape" viewBox="0 0 1456 662" width="1456" height="662" aria-hidden="true">
    <path d="M715,87 Q715,27 775,27 H1456 V662 H0 V612 H665 Q715,612 715,562 Z" fill="#1c1c1e"/>
  </svg>

  <div class="info">
    <p class="desc">Your Company Description/Goals (Optional)</p>
    <p><b>Suggested Use:</b> Take 2 Gummies per day. Do not exceed suggested dosage.</p>
    <p><b>WARNING:</b> Intended for use by adults 18 years of age and over. Do not use if the seal is broken. If you are pregnant, nursing, taking any medications or have any medical condition, consult your doctor before use.</p>
    <p class="storage"><b>Storage:</b> Store in a cool, dry place away from heat<br>and moisture.</p>
  </div>
  <div class="disclaimer"><span>*These statements have not been evaluated by the Food<br>and Drug Administration. This product is not intended to<br>diagnose, treat, cure, or prevent any disease.</span></div>
  <div class="barcode-box">YOUR BARCODE</div>
  <div class="maker">Manufactured for:<br>Your Company Name<br>Company Street Address<br>City,State,Zip<br>Phone Number<br>(Optional),Website<br>(Optional), Email (Optional)</div>

  <div class="vertical extra-strength">Extra Strength</div>
  <div class="vertical product-name">Zentaric</div>
  <div class="vertical category">Male Enhancement<br>Supplement</div>
  <div class="vertical dose">1200mg</div>

  <ul class="benefits">
    <li>VIRILITY</li>
    <li>VITALITY</li>
    <li>VIGOR</li>
  </ul>

  <div class="facts">
    <h2>SUPPLEMENT FACTS</h2>
    <div class="serving"><span>Serving Size : 2 Capsules</span><span>Serving Per Container : 30</span></div>
    <div class="amount-head"><span>Amount Per Serving</span><span>%Daily Value</span></div>
    <div class="row" style="height:56px">Horny Goat Weed Extract<small>(Epimedium sagittatum) aerial plant)</small><small>(providing 10mg of icariins)</small><span class="amt">1000 mg</span><span class="dv">*</span></div>
    <div class="row" style="height:27px">Maca Root Powder<span class="amt">250 mg</span><span class="dv">*</span></div>
    <div class="row" style="height:37px">Tribulus terrestris 40% Extract<small>(aerial parts)</small><span class="amt">60 mg</span><span class="dv">*</span></div>
    <div class="row" style="height:37px">Polypodium vulgare Powder<small>(root &amp; rhizome)</small><span class="amt">20 mg</span><span class="dv">*</span></div>
    <div class="row" style="height:36px">Tongkat Ali Root Powder<small>(Eurycoma longifolia)</small><span class="amt">100 mg</span><span class="dv">*</span></div>
    <div class="row" style="height:27px">Saw Palmetto Berry Powder<span class="amt">100 mg</span><span class="dv">*</span></div>
    <div class="row" style="height:26px">Muria Puama Root Powder<span class="amt">20 mg</span><span class="dv">*</span></div>
    <div class="row" style="height:26px">L-Arginine ( L-Arginine HCl)<span class="amt">20 mg</span><span class="dv">*</span></div>
    <div class="row" style="height:24px;border-bottom:none">Panax ginseng root powder<span class="amt">100 mg</span><span class="dv">*</span></div>
    <p class="note">* Daily Value not established</p>
  </div>
  <p class="other">Other Ingredients : Rice flour, Gelatin (bovine), and vegetable magnesium stearate</p>
  <div class="badges" role="img" aria-label="Quality certification badges">
    <span></span><span></span><span></span><span></span>
  </div>

  <div class="footer">
    <span class="count">60 CAPSULES</span>
    <i class="divider"></i>
    <span class="kind">DIETARY SUPPLEMENT</span>
  </div>
</div>
</body>
</html>
```